Design eBook Cover for Homeowner Association (HOA) book

We need a cover design for an eBook entitled "The Residents Council Leader's Manual: Practical Steps and Proven Methods".

Title: The Residents Council Leader's Manual

Subtitle: Practical Steps and Proven Methods

Name of Author: Gerald Whitcombe, CMA

Style: Professional Guide

Testimonial: "This book is an indispensable tool for anyone on an HOA board. The expert advice and practical approach in 'The Residents Council Leader's Manual' have made a world of difference in our community. Every board member should have a copy!"
— Marla Quint, HOA Board President

I have uploaded a file as design inspiration but not locked into the colors or look. Just want a clean, professional looking cover.

Target Market(s)

Board members of HOAs (Homeowners associations) in the United States

Industry/Entity Type

Real Estate, HOA

Requirements
Must have
• Clean, professional appearance that conveys authority

```html
<!DOCTYPE html>
<html lang="en">
<head>
<meta charset="utf-8">
<title>The Residents Council Leader's Manual — Cover</title>
<link rel="stylesheet" href="https://fonts.googleapis.com/css2?family=Arimo:wght@400;700&family=Great+Vibes&display=swap">
<style>
  :root {
    --page: #ffffff;
    --navy: #001f4e;
    --navy-soft: #0d3168;
    --sky: #35aaf0;
    --white: #f7f8fa;
    --rule: #c9d3e2;
  }
  html, body {
    margin: 0;
    width: 1200px;
    height: 1200px;
    overflow: hidden;
    background: var(--page);
  }
  .canvas {
    position: relative;
    width: 1200px;
    height: 1200px;
    background: var(--page);
    font-family: "Arimo", Arial, sans-serif;
  }
  .cover {
    position: absolute;
    left: 200px;
    top: 0;
    width: 812px;
    height: 1200px;
    background: var(--navy);
    color: var(--white);
  }
  .testimonial {
    position: absolute;
    left: 90px;
    width: 632px;
    top: 63px;
    margin: 0;
    text-align: center;
  }
  .testimonial-quote {
    margin: 0;
    font-size: 15px;
    line-height: 21.5px;
    color: var(--white);
  }
  .testimonial-source {
    margin: 4px 0 0;
    font-size: 15.5px;
    font-weight: 700;
    color: var(--sky);
  }
  .title {
    position: absolute;
    left: 0;
    top: 230px;
    width: 812px;
    height: 600px;
  }
  .title-word { font-family: "Arimo", Arial, sans-serif; }
  .title-article { font-family: "Great Vibes", cursive; }
  .subtitle {
    position: absolute;
    left: 90px;
    top: 877px;
    width: 636px;
    height: 138px;
    border-top: 1.5px solid var(--rule);
    border-bottom: 1.5px solid var(--rule);
    box-sizing: border-box;
    margin: 0;
    display: flex;
    align-items: center;
    justify-content: center;
    text-align: center;
    font-size: 47px;
    line-height: 58px;
    font-weight: 400;
    color: var(--sky);
  }
  .author {
    position: absolute;
    left: 0;
    width: 812px;
    top: 1082px;
    margin: 0;
    text-align: center;
    font-size: 54px;
    letter-spacing: 2px;
    color: var(--white);
  }
  .author-name { font-weight: 700; }
  .author-credential { font-weight: 400; }
</style>
</head>
<body>
<div class="canvas">
  <main class="cover">
    <blockquote class="testimonial">
      <p class="testimonial-quote">" This book is an indispensable tool for anyone on an HOA board. The expert advice and practical approach in 'The Residents Council Leader's Manual' have made a world of difference in our community. Every board member should have a copy! "</p>
      <p class="testimonial-source">— Marla Quint, HOA Board President</p>
    </blockquote>

    <svg class="title" viewBox="0 0 812 600" role="heading" aria-level="1" aria-label="The Residents Council Leader's Manual">
      <circle cx="140" cy="78" r="48" fill="var(--white)"/>
      <text class="title-article" x="140" y="96" text-anchor="middle" font-size="56" fill="var(--navy)">the</text>
      <text class="title-word" x="205" y="115" textLength="520" lengthAdjust="spacingAndGlyphs" font-size="104" fill="var(--white)">RESIDENTS</text>
      <text class="title-word" x="95" y="250" textLength="465" lengthAdjust="spacingAndGlyphs" font-size="142" fill="var(--white)">COUNCIL</text>
      <rect x="585" y="140" width="140" height="110" fill="var(--navy-soft)" role="img" aria-label="Outline icon of two house roofs with a small window"/>
      <text class="title-word" x="95" y="400" textLength="630" lengthAdjust="spacingAndGlyphs" font-size="162" font-weight="700" fill="var(--sky)">LEADER'S</text>
      <text class="title-word" x="95" y="560" textLength="630" lengthAdjust="spacingAndGlyphs" font-size="150" fill="var(--white)">MANUAL</text>
    </svg>

    <h2 class="subtitle">Practical Steps and<br>Proven Methods</h2>

    <p class="author"><span class="author-name">GERALD WHITCOMBE,</span> <span class="author-credential">CMA</span></p>
  </main>
</div>
</body>
</html>
```